Real Estate Sales Brokerage

Design a modern and fresh looking standard size business card, incorporate our logo's color scheme and modern appearance with head shot photo on front side and incorporate our log on the back side

Target Market(s)

Residential Home sales

Industry/Entity Type

Real Estate Agent

Font styles to use
Sans Serif

Colors

Designer to choose colors to be used in the design.

Requirements
Must have
• fresh, modern, not too busy, incorporate head shot in front of the card, incorporate logo in front and back of the card. Use logo design scheme as appropriate.
Nice to have
• horizontal and vertical options to compare would be nice.

```html
<!DOCTYPE html>
<html lang="en">
<head>
<meta charset="utf-8">
<title>Harbor Keystone Realty – Business Cards</title>
<link rel="stylesheet" href="https://fonts.googleapis.com/css2?family=Libre+Baskerville:wght@400;700&display=swap">
<style>
  :root {
    --olive: #59552a;
    --olive-light: #67622f;
    --yellow: #f3d344;
    --white: #ffffff;
    --paper-grey: #f0f0f0;
    --stage: #e6e6e3;
    --photo-warm: #b89a80;
    --photo-cool: #3f5a6e;
  }
  * { margin: 0; padding: 0; box-sizing: border-box; }
  html, body {
    width: 1200px;
    height: 863px;
    overflow: hidden;
    background: var(--stage);
    font-family: "Libre Baskerville", "Times New Roman", serif;
  }
  .card {
    position: absolute;
    top: 134px;
    width: 340px;
    height: 595px;
    overflow: hidden;
    box-shadow: 0 10px 28px rgba(0,0,0,0.18);
  }
  .card--front { left: 240px; background: var(--white); }
  .card--back  { left: 620px; background: var(--paper-grey); }
  .card__art {
    position: absolute;
    inset: 0;
    width: 100%;
    height: 100%;
  }
  .contact {
    position: absolute;
    left: 30px;
    bottom: 40px;
    color: var(--white);
  }
  .contact__name {
    color: var(--yellow);
    font-weight: 700;
    font-size: 21px;
    line-height: 1.1;
  }
  .contact__role {
    font-weight: 700;
    font-size: 14px;
    margin: 4px 0 22px;
  }
  .contact__line {
    font-size: 13px;
    line-height: 1.6;
  }
  .brand {
    position: absolute;
    top: 58px;
    left: 30px;
    display: flex;
    align-items: center;
    gap: 10px;
    color: var(--olive);
  }
  .brand__square {
    width: 22px;
    height: 22px;
    background: var(--olive);
    flex: none;
  }
  .brand__name {
    font-size: 15px;
    font-weight: 400;
    line-height: 1.15;
    text-transform: uppercase;
    letter-spacing: 0.02em;
  }
</style>
</head>
<body>

<section class="card card--front" aria-label="Business card front">
  <svg class="card__art" viewBox="0 0 340 595" aria-hidden="false">
    <defs>
      <linearGradient id="headshot-tone" x1="0" y1="0" x2="1" y2="1">
        <stop offset="0" stop-color="var(--photo-cool)"/>
        <stop offset="0.55" stop-color="var(--photo-warm)"/>
        <stop offset="1" stop-color="var(--photo-cool)"/>
      </linearGradient>
      <linearGradient id="olive-shade" x1="0" y1="0" x2="0" y2="1">
        <stop offset="0" stop-color="var(--olive-light)"/>
        <stop offset="1" stop-color="var(--olive)"/>
      </linearGradient>
    </defs>
    <g transform="translate(170 297.5) rotate(-20)">
      <rect class="shape-olive" x="-600" y="-115" width="695" height="800" fill="url(#olive-shade)"/>
      <rect class="shape-yellow-square" x="125" y="-100" width="110" height="110" fill="var(--yellow)"/>
      <rect class="shape-yellow-corner" x="125" y="-500" width="300" height="370" fill="var(--yellow)"/>
      <rect class="photo-frame" x="-85" y="-225" width="190" height="125" fill="var(--white)"/>
      <rect class="headshot" x="-77" y="-217" width="174" height="109" fill="url(#headshot-tone)"
            role="img" aria-label="Headshot photo of the agent"/>
    </g>
  </svg>
  <div class="contact">
    <p class="contact__name">Lorem Ipsum</p>
    <p class="contact__role">Director</p>
    <p class="contact__line">123 456 7890</p>
    <p class="contact__line">www.yoursite.com</p>
    <p class="contact__line">email_add@domain.com</p>
  </div>
</section>

<section class="card card--back" aria-label="Business card back">
  <svg class="card__art" viewBox="0 0 340 595" aria-hidden="true">
    <polygon class="band-white" points="0,185 340,525 340,595 0,595" fill="var(--white)"/>
    <polygon class="shape-yellow-square" points="-24.7,183.2 88.4,296.3 -24.7,409.4 -137.9,296.3" fill="var(--yellow)"/>
    <polygon class="shape-olive-square" points="113.1,319.3 219.2,425.4 113.1,531.4 7.1,425.4" fill="var(--olive-light)"/>
    <polygon class="shape-olive-corner" points="0,495 0,595 100,595" fill="var(--olive)"/>
  </svg>
  <div class="brand">
    <span class="brand__square"></span>
    <span class="brand__name">Harbor Keystone<br>Realty</span>
  </div>
</section>

</body>
</html>
```